Professional Photography Business cards

I need business cards that include my logo which I have uploaded. I run a photography business. I am open to ideas but I would like one side to have my logo and the other side to have my contact info. I don't have a website made but I do own a website domain. I have uploaded 2 different logo color schemes. My business colors are Blue, black , and white.

Business Name
Business Phone Number
Business Email
Business Website address
Instagram

Industry/Entity Type

Professional Photography

Contact Information for Business Card

Phone Number: 555-314-8027 email: info@tkellan-studios.example Instagram: @t.kellanstudios website doman- www.tkellan-studios.example

Requirements
Must have
• I like the idea of a business card with a full black background front and back of card. My colors must include royal blue, black, and white

```html
<!DOCTYPE html>
<html lang="en">
<head>
<meta charset="UTF-8">
<title>T. Kellan Studios – Business Card</title>
<link href="https://fonts.googleapis.com/css2?family=Montserrat:wght@400;500;700&display=swap" rel="stylesheet">
<style>
  :root {
    --royal-blue: #1a1fa8;
    --deep-blue: #0c109a;
    --soft-blue: #3a40c4;
    --ink: #0a0a0a;
    --paper: #ffffff;
    --paper-shade: #e4e5ea;
    --backdrop: #e9eaee;
    --muted: #2a2a2a;
  }
  * { margin: 0; padding: 0; box-sizing: border-box; }
  html, body {
    width: 1200px; height: 912px; overflow: hidden;
    background: var(--backdrop);
    font-family: "Montserrat", Arial, sans-serif;
  }
  .canvas {
    position: relative; width: 1200px; height: 912px;
    display: flex; flex-direction: column; align-items: center; justify-content: center; gap: 44px;
  }
  .card {
    position: relative; width: 700px; height: 400px;
    border-radius: 26px; overflow: hidden;
    box-shadow: 0 10px 28px rgba(0,0,0,0.18);
  }

  /* front */
  .card-front { background: var(--royal-blue); }
  .front-band {
    position: absolute; left: 0; top: 0; width: 100%; height: 96px;
    background: var(--ink); border-bottom: 8px solid var(--paper);
  }
  .front-art {
    position: absolute; left: 400px; top: 124px; width: 240px; height: 240px;
    border-radius: 28px;
    background: linear-gradient(145deg, var(--soft-blue), var(--deep-blue));
  }
  .brand {
    position: absolute; left: 60px; top: 250px;
    display: flex; align-items: center; gap: 14px;
    color: var(--paper); font-weight: 500; font-size: 28px; letter-spacing: 1px;
  }
  .brand-dot {
    width: 22px; height: 22px; border-radius: 50%;
    border: 3px solid var(--paper);
  }

  /* back */
  .card-back { background: var(--paper); }
  .back-band {
    position: absolute; left: 0; top: 0; width: 100%; height: 96px;
    background: var(--royal-blue); border-bottom: 8px solid var(--ink);
  }
  .back-art {
    position: absolute; left: 420px; top: 124px; width: 240px; height: 240px;
    border-radius: 28px;
    background: linear-gradient(145deg, var(--paper), var(--paper-shade));
  }
  .contact { position: absolute; left: 60px; top: 160px; }
  .contact-name {
    color: var(--deep-blue); font-weight: 700; font-size: 27px; letter-spacing: 1.5px;
    text-transform: uppercase; line-height: 1.05;
  }
  .contact-role { color: var(--muted); font-size: 17px; margin-top: 4px; }
  .contact-rule { width: 18px; height: 3px; background: var(--deep-blue); margin: 16px 0 12px; }
  .contact-list { list-style: none; }
  .contact-list li {
    display: flex; align-items: center; gap: 9px;
    color: var(--ink); font-size: 16px; line-height: 26px;
  }
  .contact-icon { width: 13px; height: 13px; flex: none; }
</style>
</head>
<body>
<main class="canvas">

  <section class="card card-front" aria-label="Card front">
    <div class="front-band"></div>
    <div class="front-art" role="img" aria-label="Camera lens illustration"></div>
    <div class="brand">
      <span class="brand-dot"></span>
      <span class="brand-name">T. Kellan Studios</span>
    </div>
  </section>

  <section class="card card-back" aria-label="Card back">
    <div class="back-band"></div>
    <div class="back-art" role="img" aria-label="Camera lens illustration"></div>
    <div class="contact">
      <h1 class="contact-name">Darren Hollis</h1>
      <p class="contact-role">Founder</p>
      <div class="contact-rule"></div>
      <ul class="contact-list">
        <li>
          <svg class="contact-icon" viewBox="0 0 16 16"><path d="M4 1 L6.5 4.5 L5 6.5 Q6.5 9.5 9.5 11 L11.5 9.5 L15 12 L13 15 Q6 14 1 3 Z" fill="var(--deep-blue)"/></svg>
          555-314-8027
        </li>
        <li>
          <svg class="contact-icon" viewBox="0 0 16 16"><rect x="1.5" y="3.5" width="13" height="9" fill="none" stroke="var(--deep-blue)" stroke-width="1.6"/><path d="M1.5 3.5 L8 9 L14.5 3.5" fill="none" stroke="var(--deep-blue)" stroke-width="1.6"/></svg>
          info@tkellan-studios.example
        </li>
        <li>
          <svg class="contact-icon" viewBox="0 0 16 16"><rect x="2" y="2" width="12" height="12" rx="2" fill="var(--deep-blue)"/></svg>
          @t.kellanstudios
        </li>
        <li>
          <svg class="contact-icon" viewBox="0 0 16 16"><circle cx="8" cy="8" r="6.5" fill="none" stroke="var(--deep-blue)" stroke-width="1.5"/><ellipse cx="8" cy="8" rx="2.8" ry="6.5" fill="none" stroke="var(--deep-blue)" stroke-width="1.2"/><path d="M1.5 8 H14.5" stroke="var(--deep-blue)" stroke-width="1.2"/></svg>
          www.tkellan-studios.example
        </li>
      </ul>
    </div>
  </section>

</main>
</body>
</html>
```